Green Logistics / Last Mile Delivery Firm needs cool one-page website

FYI - We do have a detailed brief in the uploaded files section below
COMPANY
We recently launched the company Brook Logistics which is a pioneer in urban green logistics and provides zero-emissions last mile delivery services (i.e. delivery of parcels with delivery vans to the doorstep of households) for its logistics and retail clients.
We take on urban parcel delivery for our clients with a 100% electric commercial vehicles fleet, fair and sustainable working conditions for our employees and an unparalleled professional and customer-focused mindset.
WEBSITE
In the detailed brief, we have provided examples to emulate. We need the design + coding of the website. Website needs to be friendly/optimized for and should open swiftly on both Android & iOS.
In general, the website should convey
- green mission of the company
- sustainability (good working conditions, focus on employees)
- customer orientation
- professionalism
DESIGN
In the detailed brief, we have provided designs to emulate.
Color design: we do have a logo which features 2 green colors (one lighter and one darker color tone). However, the colors on the website do not necessarily need to follow these 2 colors exactly as we are able to switch the logo colors.
Imagery: should reflect maybe 50% green/leaf/tree , 25% customer and employee orientation, and 25% logistics (here it's important that it is the last mile delivery, i.e. delivery with delivery vans to the doorstep of households)
Coding

```html
<!DOCTYPE html>
<html lang="en">
<head>
<meta charset="utf-8">
<title>Brook Logistics – Sustainable Last Mile</title>
<link rel="stylesheet" href="https://fonts.googleapis.com/css2?family=Montserrat:wght@400;500;600;700&family=Lato:wght@400;700&display=swap">
<style>
:root{
  --green:#2f9e3d;
  --green-dark:#23852f;
  --green-light:#8cc63f;
  --green-soft:#f5f9ec;
  --ink:#2b2b2b;
  --text:#555;
  --muted:#8a8a8a;
  --dark:#2a2a2a;
  --line:#dcdcdc;
  --white:#fff;
}
*{box-sizing:border-box;margin:0;padding:0}
html,body{width:1200px;height:4812px;overflow:hidden}
body{font-family:"Lato",sans-serif;color:var(--text);background:var(--white);font-size:11px;line-height:1.9}
h1,h2,h3,h4,.mont{font-family:"Montserrat",sans-serif}
section,header,footer{position:relative;width:1200px}
.abs{position:absolute}
.eyebrow{font-family:"Montserrat",sans-serif;font-size:9px;color:var(--green);text-transform:uppercase;letter-spacing:.3px}
.title{font-family:"Montserrat",sans-serif;font-weight:500;color:var(--ink);font-size:24px;line-height:1.2}
.ph{display:block}

/* hero */
.hero{height:787px;background:linear-gradient(160deg,#5d6a4c 0%,#3e4a36 35%,#2e3a2b 60%,#24302a 100%);overflow:hidden}
.hero-shade{position:absolute;inset:0;background:rgba(0,0,0,.28)}
.topbar{position:absolute;top:0;left:0;width:1200px;height:34px;background:rgba(20,20,20,.55);color:var(--white);font-size:11px}
.topbar .item{position:absolute;top:9px;display:flex;align-items:center;gap:8px;line-height:16px}
.navbar{position:absolute;top:34px;left:0;width:1200px;height:91px;background:rgba(40,40,40,.55)}
.logo{display:flex;align-items:center;gap:8px;font-family:"Montserrat",sans-serif;font-weight:600;color:var(--green-light);font-size:14px;letter-spacing:.3px}
.logo .mark{width:26px;height:26px;border-radius:50%;background:var(--green-light)}
.nav{position:absolute;top:38px;right:160px;display:flex;font-family:"Montserrat",sans-serif;font-size:11px;font-weight:500;color:var(--white);line-height:14px}
.nav span{padding:0 16px;border-left:1px solid rgba(255,255,255,.35)}
.nav span:first-child{border-left:0;color:var(--green-light)}
.nav span:last-child{padding-right:0}
.hero-tag{position:absolute;top:335px;left:0;width:1200px;text-align:center}
.hero-tag span{background:rgba(0,0,0,.55);color:#ddd;font-family:"Montserrat",sans-serif;font-size:10px;letter-spacing:5px;padding:2px 6px}
.hero h1{position:absolute;top:356px;left:0;width:1200px;text-align:center;color:var(--white);font-size:39px;font-weight:700;letter-spacing:.5px}
.hero p{position:absolute;top:434px;left:300px;width:600px;text-align:center;color:var(--white);font-size:14.5px;line-height:23px}
.btn{display:inline-block;background:var(--green);color:var(--white);font-family:"Montserrat",sans-serif;font-weight:600;font-size:10px;text-align:center}
.hero .btn{position:absolute;top:527px;left:536px;width:128px;height:40px;line-height:40px}
.arrow{position:absolute;top:400px}
.dots{position:absolute;top:745px;left:552px;display:flex;gap:6px}
.dots i{display:block;width:24px;height:2px;background:rgba(255,255,255,.5)}
.dots i.on{width:36px;background:var(--white)}

/* features */
.features{height:138px;background:#f3f3f3}
.plant{position:absolute;left:140px;top:-14px;width:178px;height:170px;border-radius:50%;background:radial-gradient(circle at 45% 45%,#7fbf4a,#4b8d2e 65%,rgba(75,141,46,0) 72%)}
.feature{position:absolute;top:40px;width:200px;display:flex;gap:10px}
.feature .num{font-family:"Montserrat",sans-serif;font-size:30px;font-weight:500;color:transparent;-webkit-text-stroke:1.3px var(--green);line-height:1}
.feature h4{font-size:12px;font-weight:500;color:var(--ink);line-height:16px}
.feature p{font-size:9.5px;color:var(--muted);line-height:17px}

/* about */
.about{height:490px}
.tabs{display:flex;font-family:"Montserrat",sans-serif;font-size:10.5px;color:#aaa;line-height:14px}
.tabs span{padding:0 14px;border-left:1px solid var(--line)}
.tabs span:first-child{padding-left:0;border:0;color:var(--green)}
.about p{font-size:10.5px;line-height:22px}
.bullets{list-style:none;font-size:10.5px;color:var(--ink)}
.bullets li{position:relative;padding-left:14px;line-height:25.5px}
.bullets li::before{content:"";position:absolute;left:0;top:10px;width:6px;height:6px;border-radius:50%;background:var(--green-light)}
.about-swoosh{position:absolute;left:720px;top:-10px;width:440px;height:360px;border-radius:50% 0 0 50%;background:linear-gradient(90deg,#fff 0%,#f4f4f4 100%)}

/* compare */
.compare{height:697px;background:linear-gradient(150deg,#3a4036 0%,#262a25 40%,#2c3b2a 100%)}
.ctable{position:absolute;left:164px;top:76px;width:571px;border:2px solid var(--white);border-collapse:collapse;color:var(--white);font-size:11.5px;text-align:center}
.ctable th{height:56px;background:var(--green);font-family:"Montserrat",sans-serif;font-weight:600;font-size:13px;border:2px solid var(--white)}
.ctable td{border:2px solid var(--white);height:43px;font-weight:400}
.ctable td.img{height:268px;padding:0}
.ctable .old{text-decoration:line-through}
.cside h3{font-size:22px;font-weight:600;color:var(--white);line-height:37px}
.cside h3.g{color:var(--green-light)}
.cside p{color:#e5e5e5;font-size:11px;line-height:22.5px}

/* services */
.services{height:677px;background:var(--white)}
.center{text-align:center;width:1200px;left:0}
.card{position:absolute;top:239px;width:203px}
.card .label{height:43px;background:#86c04b;color:var(--white);font-family:"Montserrat",sans-serif;font-size:10px;font-weight:600;line-height:43px;text-align:center;text-transform:uppercase}
.card p{margin-top:16px;font-size:10.5px;line-height:22.5px;color:var(--text)}

/* cta */
.cta{height:226px;background:linear-gradient(90deg,#2a9538,#38a746)}
.cta h2{font-size:23px;font-weight:700;color:var(--white)}
.cta p{color:var(--white);font-size:10.5px;line-height:23px}
.outline{border:1.5px solid var(--white);color:var(--white);font-family:"Montserrat",sans-serif;font-size:10px;font-weight:600;text-align:center}

/* careers */
.careers{height:920px;background:var(--green-soft)}
.careers p.body{font-size:10.5px;line-height:22.5px}
.jobbar{position:absolute;left:161px;top:407px;width:878px;height:75px;background:var(--green);color:var(--white)}
.acc{position:absolute;left:161px;width:878px;font-family:"Montserrat",sans-serif;font-size:12px;font-weight:500;color:var(--ink);display:flex;justify-content:space-between}
.acc.open{color:var(--green)}
.rule{position:absolute;left:161px;width:878px;height:1px;background:var(--line)}
.reqs{list-style:none;font-size:10.5px;line-height:25.5px;color:var(--ink)}
.reqs li::before{content:"- "}

/* contact */
.contact{height:523px;background:var(--white)}
.info{position:absolute;left:161px;display:flex;gap:14px}
.info h4{font-family:"Montserrat",sans-serif;font-size:11.5px;font-weight:500;color:var(--ink);line-height:16px}
.info p{font-size:10px;line-height:17px}
.field{position:absolute;border:1px solid var(--line);background:var(--white);font-size:10px;color:#999;padding:9px 14px;line-height:16px}

/* footer */
.footer{height:308px;background:#f7faf1}
.footer h4{font-family:"Montserrat",sans-serif;font-size:15px;font-weight:500;color:var(--ink)}
.flinks{list-style:none;font-size:10.5px;color:var(--ink);line-height:30.5px}
.social{display:flex;gap:8px}
.social i{display:block;width:28px;height:28px;background:#cfd6c9}
.social i.on{background:var(--green)}
.copy{height:46px;background:var(--green);color:var(--white);text-align:center;font-size:11px;line-height:46px}
</style>
</head>
<body>

<header class="hero">
  <div class="ph abs" role="img" aria-label="Electric delivery van driving along a tree-lined road" style="inset:0;background:linear-gradient(120deg,#8a9674 0%,#55634a 40%,#2f3a2d 75%,#1f271f 100%)"></div>
  <div class="hero-shade"></div>
  <div class="topbar">
    <div class="item" style="left:161px">
      <svg width="10" height="10" viewBox="0 0 24 24"><path fill="#fff" d="M6.6 10.8a15 15 0 006.6 6.6l2.2-2.2c.3-.3.7-.4 1-.2 1.1.4 2.3.6 3.6.6.6 0 1 .4 1 1V20c0 .6-.4 1-1 1A17 17 0 013 4c0-.6.4-1 1-1h3.5c.6 0 1 .4 1 1 0 1.3.2 2.5.6 3.6.1.3 0 .7-.2 1z"/></svg>
      555 018 2640
      <span style="opacity:.5;margin:0 6px">|</span>
      <svg width="11" height="9" viewBox="0 0 24 18"><rect x="1" y="1" width="22" height="16" fill="none" stroke="#fff" stroke-width="2"/><path d="M1 1l11 9 11-9" fill="none" stroke="#fff" stroke-width="2"/></svg>
      hello@brookmail.net
    </div>
    <div class="item" style="right:161px">EN
      <svg width="8" height="6" viewBox="0 0 8 6"><path d="M1 1l3 3 3-3" stroke="#fff" fill="none" stroke-width="1.3"/></svg>
    </div>
  </div>
  <div class="navbar">
    <div class="logo abs" style="left:161px;top:30px"><span class="mark"></span>BROOK LOGISTICS</div>
    <nav class="nav"><span>HOME</span><span>ABOUT</span><span>SERVICES</span><span>CAREERS</span><span>CONTACT</span></nav>
  </div>
  <div class="hero-tag"><span>BECAUSE WE CARE ABOUT TREES</span></div>
  <h1>BROOK LOGISTICS - SUSTAINABLE LAST MILE</h1>
  <p>Lorem Ipsum is simply dummy text of the printing and typesetting industry. Lorem Ipsum has been the industry's standard dummy text ever since the 1500s.</p>
  <a class="btn">GET STARTED</a>
  <svg class="arrow" style="left:70px" width="24" height="20" viewBox="0 0 24 20"><path d="M22 10H3M10 3l-7 7 7 7" stroke="#fff" stroke-width="1.6" fill="none"/></svg>
  <svg class="arrow" style="left:1106px" width="24" height="20" viewBox="0 0 24 20"><path d="M2 10h19M14 3l7 7-7 7" stroke="#fff" stroke-width="1.6" fill="none"/></svg>
  <div class="dots"><i></i><i class="on"></i><i></i></div>
</header>

<section class="features">
  <div class="plant" role="img" aria-label="Leafy green plant"></div>
  <div class="feature" style="left:391px"><div class="num">01</div><div><h4>FEATURE I</h4><p>Lorem Ipsum is simply dummy text of the printing.</p></div></div>
  <div class="feature" style="left:613px"><div class="num">02</div><div><h4>FEATURE II</h4><p>Lorem Ipsum is simply dummy text of the printing.</p></div></div>
  <div class="feature" style="left:836px"><div class="num">03</div><div><h4>FEATURE III</h4><p>Lorem Ipsum is simply dummy text of the printing.</p></div></div>
</section>

<section class="about">
  <div class="about-swoosh"></div>
  <div class="eyebrow abs" style="left:161px;top:60px">Introduction</div>
  <h2 class="title abs" style="left:161px;top:78px">Few Words About Us</h2>
  <div class="tabs abs" style="left:161px;top:146px"><span>WHO WE ARE</span><span>OUR MISSION</span><span>OUR VALUES</span></div>
  <p class="abs" style="left:161px;top:180px;width:420px">Brook Logistics is a pioneer in urban green logistics and provides zero-emissions last mile delivery services for its logistics and retail clients.</p>
  <ul class="bullets abs" style="left:161px;top:236px">
    <li>Lorem Ipsum Dolor</li>
    <li>Dolor Amet Ningun Postel</li>
    <li>Text Filler For Design Purposes</li>
    <li>Another Text Filler For Design Purposes</li>
  </ul>
  <p class="abs" style="left:161px;top:350px;width:420px">We take on urban parcel delivery for our clients with a 100% electric commercial vehicles fleet, fair and the sustainable working conditions for our employees and an unparalleled professional and customer-focused mindset.</p>
  <div class="ph abs" role="img" aria-label="Indoor waterfall surrounded by greenery" style="left:619px;top:127px;width:209px;height:286px;background:linear-gradient(180deg,#c9d6c4,#6f8a62 55%,#3f5a39)"></div>
  <div class="ph abs" role="img" aria-label="Smiling delivery employee in green uniform holding a parcel" style="left:815px;top:56px;width:224px;height:299px;background:linear-gradient(160deg,#c7a47a,#5c8e47 55%,#2e7a33)"></div>
</section>

<section class="compare">
  <div class="ph abs" role="img" aria-label="Dark forest background" style="inset:0;background:linear-gradient(150deg,rgba(60,70,55,.6),rgba(30,35,30,.2) 50%,rgba(40,70,40,.5))"></div>
  <table class="ctable">
    <tr><th>An Ordinary Parcel Delivery Firm</th><th>A pioneering Green Last Mile</th></tr>
    <tr>
      <td class="img"><div role="img" aria-label="White delivery van" style="margin:0 auto;width:240px;height:170px;border-radius:20px;background:linear-gradient(180deg,#f2f2f2,#b9b9b9)"></div></td>
      <td class="img"><div role="img" aria-label="Green electric delivery van" style="margin:0 auto;width:230px;height:170px;border-radius:20px;background:linear-gradient(180deg,#5fd25f,#1e8f2a)"></div></td>
    </tr>
    <tr><td class="old">Polluting our cities</td><td>Delivering parcels emissions-free</td></tr>
    <tr><td class="old">Always in a rush</td><td>Putting customer experience first</td></tr>
    <tr><td class="old">Short-term oriented</td><td>Operating the business sustainably</td></tr>
    <tr><td class="old">Focusing on profit only</td><td>Focued on environment, customers&amp;employees</td></tr>
    <tr><td class="old">Yet another parcel delivery firm</td><td>A professional services company</td></tr>
  </table>
  <div class="cside abs" style="left:781px;top:150px;width:260px">
    <h3>Ordinary Firms</h3><h3>vs</h3><h3 class="g">Brook Logistics</h3>
    <p style="margin-top:14px">Lorem Ipsum is simply dummy text of the and printing and typesetting industry. Lorem Ipsum has been the industry's standard dummy text ever since the 1500s, when an unknown printer took a galley of type and scrambled it to make a type specimen book. It has survived not only five centuries, but also the leap into electronic type, remaining essentially unchanged.</p>
    <p style="margin-top:14px">Lorem Ipsum is simply dummy text of the and printing and typesetting industry. Lorem Ipsum has been the industry's standard dummy text.</p>
  </div>
</section>

<section class="services">
  <div class="eyebrow abs center" style="top:72px">What we offer</div>
  <h2 class="title abs center" style="top:94px;font-size:27px">Our Services</h2>
  <p class="abs" style="left:161px;top:162px;width:878px;text-align:center;font-size:10.5px;line-height:19px">Brook Logistics provides last mile delivery services in urban areas to clients in the logistics and retail space. Our permanent employees are all highly trained and commit to highest professional standards which we continuously review and further develop with them.</p>
  <div class="card" style="left:161px"><div role="img" aria-label="Electric delivery van parked in the street" style="height:241px;background:linear-gradient(160deg,#6c8a5c,#2d5a34 60%,#1f3a24)"></div><div class="label">Zero-Emission Delivery</div><p>We usually operate with a 100% electric commercial vehicle fleet</p></div>
  <div class="card" style="left:387px"><div role="img" aria-label="Delivery driver at the wheel of a van" style="height:241px;background:linear-gradient(160deg,#e8ece6,#9fc48f 50%,#3f9c3a)"></div><div class="label">Highly Trained Drivers</div><p>We only employ permanently, train far above average, and live a great team spirit</p></div>
  <div class="card" style="left:613px"><div role="img" aria-label="Delivery employee carrying a parcel" style="height:241px;background:linear-gradient(160deg,#f1f1f1,#c7d6bd 45%,#4aa845)"></div><div class="label">Professional All Around</div><p>We honor our commitments and hold ourselves to the highest professional standards</p></div>
  <div class="card" style="left:837px"><div role="img" aria-label="Parcel handed over at a customer's doorstep" style="height:241px;background:linear-gradient(160deg,#d9d4cc,#8f9e84 50%,#3d8f3c)"></div><div class="label">Unparalleled Customer Care</div><p>We live a customer-oriented mindset, always measuring ourselves against their experience</p></div>
</section>

<section class="cta">
  <h2 class="abs" style="left:161px;top:72px">Get In Touch With Brook Logistics!</h2>
  <p class="abs" style="left:161px;top:110px;width:580px">If you got excited, or have a question about our services, our approach, our jobs or just want to get in touch to chat about how green logistics can make the planet a little bit better, please get in touch!</p>
  <div class="outline abs" style="left:910px;top:91px;width:129px;height:45px;line-height:42px">CONTACT US</div>
</section>

<section class="careers">
  <div class="eyebrow abs center" style="top:78px">Want to join us?</div>
  <h2 class="title abs center" style="top:98px;font-size:27px">Careers</h2>
  <div class="abs" style="left:161px;top:184px;width:878px">
    <p class="body">If you join Brook Logistics, you join a family. We elevate one another, care for each other's wellbeing and growth, and celebrate our successes. We strongly believe growth is a team sport and that every member of the family fully contributes to the achievements of the company overall.</p>
    <p class="body" style="margin-top:12px">At the heart of everything we do at Brook Logistics is a relentless focus on our mission. That's why we aim to ensure our employees can follow their own passion at the workplace, be this working in a truly collaborative and caring team, putting a smile on a customer's face or making the world a better place.</p>
    <p class="body" style="margin-top:12px">While we are helping our clients grow by delivering their parcels, we are also helping all our employees grow personally and professionally. We care about our employees' happiness and wellbeing which we provide additional benefits like supplementary health insurance.</p>
    <p class="body" style="margin-top:12px">If you are excited about joining our Brook Logistics family, please check out our open positions.</p>
  </div>
  <div class="jobbar">
    <div class="abs mont" style="left:28px;top:26px;font-size:15px;font-weight:600">Full-time driver / parcel deliverer (m/f/d) for Berlin</div>
    <div class="abs" style="left:520px;top:15px;width:340px;font-size:9.5px;line-height:22px">As a partner for our clients, we are looking for additional members of the Brook Logistics Family in Berlin as soon as possible.</div>
  </div>
  <div class="acc" style="top:514px"><span>Your tasks as a delivery driver:</span><span style="font-size:16px;color:#777">+</span></div>
  <div class="rule" style="top:544px"></div>
  <div class="acc open" style="top:560px"><span>Required knowledge and skills:</span><span style="font-size:16px">−</span></div>
  <ul class="reqs abs" style="left:161px;top:590px">
    <li>Enjoy driving and dealing with customers</li>
    <li>Reliability, willingness to learn, and flexibility</li>
    <li>Customer orientation, teamwork and motivation</li>
    <li>Class B driving license and driving experience</li>
    <li>Certificate of good conduct without entries</li>
  </ul>
  <div class="rule" style="top:725px"></div>
  <div class="acc" style="top:734px"><span>What you can expect from the Brook Logistics family:</span><span style="font-size:16px;color:#777">+</span></div>
  <div class="rule" style="top:766px"></div>
  <p class="abs center" style="top:821px;font-size:11.5px;color:var(--ink)">Interested? <u>Send us an email</u> or <u>give us a call</u>. We would like to invite you to a trial day</p>
</section>

<section class="contact">
  <div class="eyebrow abs" style="left:161px;top:70px">We'd love to hear from you!</div>
  <h2 class="title abs" style="left:161px;top:90px">Contact Us</h2>
  <p class="abs" style="left:161px;top:150px;width:420px;font-size:10.5px;line-height:22.5px">Whether you have a question about our services, our approach, our jobs or just want to get in touch to chat about how green logistics can make the planet a little bit better, our team is ready to answer your questions and enquiries</p>
  <div class="info" style="top:240px">
    <svg width="24" height="28" viewBox="0 0 24 28"><path d="M12 2a9 9 0 00-9 9c0 7 9 15 9 15s9-8 9-15a9 9 0 00-9-9z" fill="none" stroke="#8cc63f" stroke-width="1.5"/><circle cx="12" cy="11" r="3.5" fill="none" stroke="#8cc63f" stroke-width="1.5"/></svg>
    <div><h4>LOCATION:</h4><p>Lorem ipsum text for design purpose only</p></div>
  </div>
  <div class="info" style="top:314px">
    <svg width="26" height="20" viewBox="0 0 26 20"><rect x="1" y="2" width="24" height="16" fill="none" stroke="#8cc63f" stroke-width="1.5"/><path d="M1 2l12 9 12-9" fill="none" stroke="#8cc63f" stroke-width="1.5"/></svg>
    <div><h4>EMAIL US AT:</h4><p>Lorem ipsum text for design purpose only</p></div>
  </div>
  <div class="info" style="top:388px">
    <svg width="26" height="26" viewBox="0 0 24 24"><path d="M6.6 10.8a15 15 0 006.6 6.6l2.2-2.2c.3-.3.7-.4 1-.2 1.1.4 2.3.6 3.6.6.6 0 1 .4 1 1V20c0 .6-.4 1-1 1A17 17 0 013 4c0-.6.4-1 1-1h3.5c.6 0 1 .4 1 1 0 1.3.2 2.5.6 3.6.1.3 0 .7-.2 1z" fill="none" stroke="#8cc63f" stroke-width="1.2"/></svg>
    <div><h4>CALL US AT:</h4><p>Lorem ipsum text for design purpose only</p></div>
  </div>
  <div class="field" style="left:620px;top:70px;width:208px;height:36px">Full Name*</div>
  <div class="field" style="left:843px;top:70px;width:205px;height:36px">Email Address*</div>
  <div class="field" style="left:620px;top:121px;width:208px;height:37px">Phone Number*</div>
  <div class="field" style="left:843px;top:121px;width:205px;height:37px">Subject*</div>
  <div class="field" style="left:620px;top:173px;width:428px;height:187px">Type your message here...</div>
  <div class="btn abs" style="left:620px;top:386px;width:208px;height:34px;line-height:34px">SEND MESSAGE</div>
</section>

<footer class="footer">
  <div class="logo abs" style="left:161px;top:56px"><span class="mark"></span>BROOK LOGISTICS</div>
  <p class="abs" style="left:161px;top:108px;width:200px;font-size:10.5px;line-height:22.5px;color:var(--ink)">Some text filler here that has been used for design purposes, in order to fill and avoid the empty spaces.</p>
  <div class="abs" style="left:161px;top:194px;font-size:10.5px;color:var(--ink);line-height:25px">
    <div><span style="color:var(--green)">&#9742;</span>&nbsp;&nbsp;555 018 2641</div>
    <div><span style="color:var(--green)">&#9993;</span>&nbsp;&nbsp;hello@brookmail.net</div>
  </div>
  <h4 class="abs" style="left:435px;top:46px">Quick Links</h4>
  <ul class="flinks abs" style="left:435px;top:89px"><li>&gt;&gt; Home</li><li>&gt;&gt; About Us</li><li>&gt;&gt; Services</li><li>&gt;&gt; Careers</li><li>&gt;&gt; Contact</li></ul>
  <h4 class="abs" style="left:645px;top:46px">Information</h4>
  <ul class="flinks abs" style="left:645px;top:89px"><li>&gt;&gt; Privacy Policy</li><li>&gt;&gt; Legal Notice</li><li>&gt;&gt; Simply Dummy Txt</li><li>&gt;&gt; Text Filler</li><li>&gt;&gt; Another Text Filler</li></ul>
  <h4 class="abs" style="left:835px;top:46px">Newsletter</h4>
  <p class="abs" style="left:835px;top:94px;font-size:10.5px;color:var(--ink)">Subscribe below to get notified!</p>
  <div class="field abs" style="left:835px;top:129px;width:170px;height:34px;font-size:9px">Your E-mail Address</div>
  <div class="abs" style="left:1004px;top:129px;width:34px;height:34px;background:var(--green-light)">
    <svg style="margin:10px" width="14" height="14" viewBox="0 0 14 14"><path d="M13 1L1 6l5 2 2 5z" fill="#fff"/></svg>
  </div>
  <div class="abs" style="left:835px;top:209px;display:flex;align-items:center;gap:12px;font-size:10.5px;color:var(--ink)">Find Us Also At:
    <div class="social"><i></i><i class="on"></i><i></i></div>
  </div>
  <div class="copy abs" style="left:0;bottom:0;width:1200px">Copyright © 2020 <b>Brook Logistics</b> - All Rights Reserved</div>
</footer>

</body>
</html>
```